Nail salon window signage design

We need new signage to be designed for our existing nail salon. The sign will be a large sticker that will stick onto the glass window at the front.

Some of the services we provide are:
Manicures
Pedicures
Velora Gel Builder
Acrylic Nails
KVT
Brenlux
Gel Polish
You may wish to have our services listed on the sign but is not compulsory.

I have also attached our logo which can be used on the sign but is not compulsory.

I have also attached a photo of the front of our salon and the sign will be where I have outlined in yellow.

The size of the sign will be 119cm wide and 170cm high.

I am open to any nice classy design you can think of.

```html
<!DOCTYPE html>
<html lang="en">
<head>
<meta charset="utf-8">
<title>Aurelia Nails – Window Signage</title>
<link rel="stylesheet" href="https://fonts.googleapis.com/css2?family=Tinos:wght@400;700&display=swap">
<style>
  :root {
    --page-bg: #d9dadb;
    --cream: #fdf9f3;
    --wine: #8e2f3a;
    --olive: #7d6a45;
    --sand: #cfc19a;
    --sand-light: #ece3ca;
    --skin: #eab9a4;
    --nail-blue: #5b5c8c;
  }
  * { margin: 0; padding: 0; box-sizing: border-box; }
  html, body {
    width: 1200px; height: 1200px; overflow: hidden;
    background: var(--page-bg);
    font-family: "Tinos", "Times New Roman", serif;
  }
  .sign {
    position: absolute; left: 250px; top: 100px;
    width: 700px; height: 1000px;
    background: var(--cream);
    overflow: hidden;
  }
  .floral-top {
    position: absolute; right: 0; top: 0; width: 377px; height: 242px;
    background: radial-gradient(ellipse at 85% 20%, var(--sand) 0%, var(--sand-light) 55%, rgba(236,227,202,0) 75%);
  }
  .floral-bottom {
    position: absolute; left: 0; bottom: 0; width: 435px; height: 292px;
    background: radial-gradient(ellipse at 10% 90%, var(--sand) 0%, var(--sand-light) 50%, rgba(236,227,202,0) 75%);
  }
  .hand-photo {
    position: absolute; right: 0; bottom: 0; width: 298px; height: 559px;
    background: linear-gradient(160deg, rgba(253,249,243,0) 0%, #f1d3c4 30%, var(--skin) 70%, #e3a892 100%);
    border-top-left-radius: 140px 200px;
  }
  .brand {
    position: absolute; left: 0; right: 0; top: 210px;
    text-align: center;
    font-weight: 700; font-size: 62px; color: var(--wine);
    letter-spacing: 1px;
  }
  .services-title {
    position: absolute; left: 152px; top: 359px;
    width: 396px; height: 49px;
    border: 1.5px solid var(--wine); border-radius: 25px;
    display: flex; align-items: center; justify-content: center;
    font-weight: 700; font-size: 27px; color: var(--wine);
  }
  .service-list {
    position: absolute; list-style: none;
  }
  .service-list.left { left: 48px; top: 455px; }
  .service-list.right { left: 483px; top: 455px; }
  .service-list li {
    display: flex; align-items: center;
    height: 49.3px;
    font-weight: 700; font-size: 27px; color: var(--olive);
  }
  .service-list svg { width: 16px; height: 16px; margin-right: 9px; fill: var(--wine); }
  .contact { position: absolute; left: 69px; top: 718px; width: 296px; }
  .contact-web {
    display: flex; align-items: center; gap: 8px;
    padding-left: 7px; padding-bottom: 4px;
    font-size: 20px; color: var(--olive);
    border-bottom: 1.5px solid var(--olive);
  }
  .contact-web svg { width: 20px; height: 20px; }
  .contact-phone {
    display: flex; align-items: center; gap: 4px;
    padding-left: 13px; margin-top: 2px;
    font-weight: 700; font-size: 33px; color: var(--olive);
  }
  .contact-phone svg { width: 24px; height: 24px; fill: var(--wine); }
</style>
</head>
<body>
  <main class="sign">
    <div class="floral-top" role="img" aria-label="Line-drawn leaves and flowers on soft sand shapes"></div>
    <div class="floral-bottom" role="img" aria-label="Line-drawn tropical leaves and flowers on soft sand shapes"></div>
    <div class="hand-photo" role="img" aria-label="Photo of a hand with blue-violet manicured nails holding a white flower"></div>

    <h1 class="brand">Aurelia Nails</h1>

    <div class="services-title">Services We Provide Are</div>

    <ul class="service-list left">
      <li><svg viewBox="0 0 24 24"><path d="M12 1l3.2 7.3 7.8.6-6 5.2 1.9 7.7L12 17.7 5.1 21.8 7 14.1 1 8.9l7.8-.6z"/></svg>Manicures</li>
      <li><svg viewBox="0 0 24 24"><path d="M12 1l3.2 7.3 7.8.6-6 5.2 1.9 7.7L12 17.7 5.1 21.8 7 14.1 1 8.9l7.8-.6z"/></svg>Pedicures</li>
      <li><svg viewBox="0 0 24 24"><path d="M12 1l3.2 7.3 7.8.6-6 5.2 1.9 7.7L12 17.7 5.1 21.8 7 14.1 1 8.9l7.8-.6z"/></svg>Velora Gel Builder</li>
      <li><svg viewBox="0 0 24 24"><path d="M12 1l3.2 7.3 7.8.6-6 5.2 1.9 7.7L12 17.7 5.1 21.8 7 14.1 1 8.9l7.8-.6z"/></svg>Acrylic Nails</li>
    </ul>
    <ul class="service-list right">
      <li><svg viewBox="0 0 24 24"><path d="M12 1l3.2 7.3 7.8.6-6 5.2 1.9 7.7L12 17.7 5.1 21.8 7 14.1 1 8.9l7.8-.6z"/></svg>KVT</li>
      <li><svg viewBox="0 0 24 24"><path d="M12 1l3.2 7.3 7.8.6-6 5.2 1.9 7.7L12 17.7 5.1 21.8 7 14.1 1 8.9l7.8-.6z"/></svg>Brenlux</li>
      <li><svg viewBox="0 0 24 24"><path d="M12 1l3.2 7.3 7.8.6-6 5.2 1.9 7.7L12 17.7 5.1 21.8 7 14.1 1 8.9l7.8-.6z"/></svg>Gel Polish</li>
    </ul>

    <div class="contact">
      <div class="contact-web">
        <svg viewBox="0 0 24 24" fill="none" stroke="#8e2f3a" stroke-width="1.5">
          <circle cx="12" cy="12" r="10.5" stroke="#7d6a45"/>
          <circle cx="12" cy="12" r="6.5"/>
          <ellipse cx="12" cy="12" rx="3" ry="6.5"/>
          <line x1="5.5" y1="12" x2="18.5" y2="12"/>
        </svg>
        <span>www.aurelianails.com.au</span>
      </div>
      <div class="contact-phone">
        <svg viewBox="0 0 24 24"><path d="M6.6 10.8a15.1 15.1 0 006.6 6.6l2.2-2.2c.3-.3.7-.4 1-.2 1.1.4 2.3.6 3.6.6.6 0 1 .4 1 1V20c0 .6-.4 1-1 1A17 17 0 013 4c0-.6.4-1 1-1h3.5c.6 0 1 .4 1 1 0 1.3.2 2.5.6 3.6.1.3 0 .7-.2 1z"/></svg>
        <span>+61 400 555 217</span>
      </div>
    </div>
  </main>
</body>
</html>
```